Graphic Design of Business Process

We require an eye-catching, sophisticated design of 2 business processes (attached), that will be used digitally AND for print (to be put on walls in our office).

The basic layout is attached. We require a creative, professional designer to re-design these so that they look appealing but still able to grasp all the information.

We will require vector files and editable project files for final delivery. You may refer to our website (kitefieldmedia.com.au) for an indication of our brand.

If you have any questions, please ask.

Thank you.

```html
<!DOCTYPE html>
<html lang="en">
<head>
<meta charset="utf-8">
<title>Sales Content Funnel</title>
<link rel="stylesheet" href="https://fonts.googleapis.com/css2?family=Source+Sans+3:wght@600;700;800&family=Fira+Sans:wght@600;700&family=Archivo+Black&family=Quicksand:wght@400&display=swap">
<style>
  :root {
    --bg-light: #e6e7e8;
    --bg-dark: #3a3a3a;
    --bg-darker: #2f2f2f;
    --red: #ea5050;
    --orange: #f7a51d;
    --green: #4caf50;
    --blue: #29b6d3;
    --purple: #7b5ea7;
    --brown-text: #b0541e;
    --green-text: #1f5e2a;
    --blue-text: #0e5470;
    --hero: #f0b41c;
    --hub: #3cb54a;
    --hygiene: #35acd9;
    --ink: #111;
  }
  html, body { margin: 0; padding: 0; overflow: hidden; }
  body { width: 958px; height: 1200px; background: var(--bg-light); }
  .poster { position: relative; width: 958px; height: 1200px; overflow: hidden; }
  .poster svg { position: absolute; left: 0; top: 0; }
  .heading { font-family: "Source Sans 3", sans-serif; font-weight: 700; }
  .body-text { font-family: "Fira Sans", sans-serif; font-weight: 600; }
  .legend-title { font-family: "Archivo Black", sans-serif; }
  .legend-sub { font-family: "Quicksand", sans-serif; font-weight: 400; }
</style>
</head>
<body>
<div class="poster">
<svg class="sales-funnel" width="958" height="1200" viewBox="0 0 958 1200" xmlns="http://www.w3.org/2000/svg">
  <defs>
    <marker id="arrowhead" viewBox="0 0 10 10" refX="6" refY="5" markerWidth="4.2" markerHeight="4.2" orient="auto-start-reverse">
      <path d="M0 0 L10 5 L0 10 Z" fill="var(--ink)"/>
    </marker>
    <clipPath id="funnel-shape">
      <polygon points="48,175 698,175 448,664 296,664"/>
    </clipPath>
  </defs>

  <!-- header swoosh -->
  <g class="header-band">
    <path d="M0 0 H958 V44 Q520 40 0 100 Z" fill="#4a4a4a"/>
    <path d="M0 0 H958 V26 Q520 22 0 70 Z" fill="var(--bg-dark)"/>
  </g>

  <!-- footer panel -->
  <g class="footer-panel">
    <rect x="0" y="724" width="958" height="476" fill="var(--bg-dark)"/>
    <polygon points="958,724 958,1200 100,1200" fill="#404040"/>
  </g>

  <!-- funnel bands -->
  <g class="funnel" clip-path="url(#funnel-shape)">
    <rect x="0" y="175" width="958" height="121" fill="var(--red)"/>
    <rect x="0" y="296" width="958" height="120" fill="var(--orange)"/>
    <rect x="0" y="416" width="958" height="120" fill="var(--green)"/>
    <rect x="0" y="536" width="958" height="128" fill="var(--blue)"/>
    <polygon points="48,175 92,175 340,664 296,664" fill="#fff" opacity="0.3"/>
    <polygon points="576,175 698,175 448,664 416,664" fill="#000" opacity="0.07"/>
  </g>

  <!-- funnel text -->
  <g class="funnel-text" text-anchor="middle" fill="#fff">
    <text class="heading" x="382" y="250" font-size="86" font-weight="800" textLength="236" lengthAdjust="spacingAndGlyphs">SALES</text>
    <text class="heading" x="382" y="285" font-size="26" textLength="180" lengthAdjust="spacingAndGlyphs">Content Funnel</text>

    <text class="heading" x="380" y="340" font-size="52" textLength="272" lengthAdjust="spacingAndGlyphs">AWARENESS</text>
    <text class="heading" x="380" y="358" font-size="16" fill="var(--brown-text)" textLength="218" lengthAdjust="spacingAndGlyphs">IDENTIFY PROBLEM/NEED</text>
    <text class="body-text" x="376" y="378" font-size="16">• Aspirational</text>
    <text class="body-text" x="376" y="402" font-size="16" textLength="296" lengthAdjust="spacingAndGlyphs">• Market The <tspan text-decoration="underline">Outcome</tspan> Not Product</text>

    <text class="heading" x="376" y="448" font-size="40" textLength="254" lengthAdjust="spacingAndGlyphs">CONSIDERATION</text>
    <text class="heading" x="376" y="466" font-size="16" fill="var(--green-text)" textLength="213" lengthAdjust="spacingAndGlyphs">EVALUATE ALTERNATIVES</text>
    <text class="body-text" x="376" y="488" font-size="15" textLength="304" lengthAdjust="spacingAndGlyphs">•Why is <tspan text-decoration="underline">this solution</tspan> better than others</text>
    <text class="body-text" x="378" y="508" font-size="15" textLength="270" lengthAdjust="spacingAndGlyphs">•<tspan text-decoration="underline">How</tspan> is the provider going to solve</text>
    <text class="body-text" x="380" y="525" font-size="15">my need</text>

    <text class="heading" x="374" y="564" font-size="24" textLength="172" lengthAdjust="spacingAndGlyphs">ACTION/DECISION</text>
    <text class="heading" x="374" y="581" font-size="14" fill="var(--blue-text)" textLength="136" lengthAdjust="spacingAndGlyphs">PRESENT AN OFFER</text>
    <text class="body-text" x="370" y="605" font-size="15">•<tspan text-decoration="underline">Which</tspan> Provider?</text>
  </g>

  <!-- connecting arrows -->
  <g class="flow-arrows" fill="none" stroke="var(--ink)" stroke-width="6" stroke-linecap="round">
    <path d="M808 482 C930 470, 930 372, 862 355" marker-start="url(#arrowhead)" marker-end="url(#arrowhead)"/>
    <path d="M752 592 C880 585, 880 505, 812 490" marker-start="url(#arrowhead)" marker-end="url(#arrowhead)"/>
    <path d="M760 600 C812 615, 812 660, 740 664 L462 664" marker-end="url(#arrowhead)"/>
  </g>

  <!-- stage boxes -->
  <g class="stage-boxes">
    <polygon class="stage-problem" points="654,308 878,308 836,404 614,404" fill="var(--orange)"/>
    <polygon class="stage-providers" points="596,442 814,442 772,534 554,534" fill="var(--green)"/>
    <polygon class="stage-convert" points="532,576 754,576 734,617 516,617" fill="var(--blue)"/>
    <polygon class="stage-referral" points="494,654 668,654 658,686 484,686" fill="var(--purple)"/>
  </g>
  <g class="stage-text">
    <text class="heading" x="654" y="336" font-size="22" fill="var(--brown-text)" textLength="204" lengthAdjust="spacingAndGlyphs">Problem &amp; Solution</text>
    <text class="body-text" x="724" y="362" font-size="17" fill="#fff" text-anchor="middle">• Subject Showing</text>
    <text class="body-text" x="636" y="381" font-size="17" fill="#fff" textLength="198" lengthAdjust="spacingAndGlyphs">Symptons of Problems</text>

    <text class="heading" x="696" y="464" font-size="21" fill="var(--green-text)" text-anchor="middle" textLength="206" lengthAdjust="spacingAndGlyphs">Providers &amp; Types of</text>
    <text class="heading" x="696" y="483" font-size="21" fill="var(--green-text)" text-anchor="middle">Solution</text>
    <text class="body-text" x="574" y="506" font-size="17" fill="#fff">•Subject Gives</text>
    <text class="body-text" x="568" y="526" font-size="17" fill="#fff">Name to Problem</text>

    <text class="heading" x="634" y="601" font-size="23" fill="var(--blue-text)" text-anchor="middle" textLength="180" lengthAdjust="spacingAndGlyphs">Convert &amp; Retain</text>
    <text class="body-text" x="574" y="675" font-size="17" fill="#fff" text-anchor="middle">Wom &amp; Referral</text>
  </g>

  <!-- content legend -->
  <g class="content-legend">
    <g class="legend-hero">
      <rect x="42" y="772" width="59" height="108" fill="var(--hero)"/>
      <rect x="101" y="877" width="468" height="3" fill="var(--hero)"/>
      <text class="legend-title" x="121" y="824" font-size="62" fill="var(--hero)">Hero</text>
      <text class="legend-sub" x="121" y="867" font-size="34" fill="var(--hero)" textLength="366" lengthAdjust="spacingAndGlyphs">Tentpole Campaigns</text>
    </g>
    <g class="legend-hub">
      <rect x="42" y="894" width="59" height="108" fill="var(--hub)"/>
      <rect x="101" y="999" width="468" height="3" fill="var(--hub)"/>
      <text class="legend-title" x="121" y="946" font-size="62" fill="var(--hub)">Hub</text>
      <text class="legend-sub" x="121" y="990" font-size="34" fill="var(--hub)" textLength="418" lengthAdjust="spacingAndGlyphs">Regular “Push” Content</text>
    </g>
    <g class="legend-hygiene">
      <rect x="42" y="1016" width="59" height="108" fill="var(--hygiene)"/>
      <rect x="101" y="1121" width="468" height="3" fill="var(--hygiene)"/>
      <text class="legend-title" x="121" y="1068" font-size="62" fill="var(--hygiene)">Hygiene</text>
      <text class="legend-sub" x="121" y="1112" font-size="34" fill="var(--hygiene)" textLength="446" lengthAdjust="spacingAndGlyphs">Always-on “Pull” Content</text>
    </g>
  </g>
</svg>
</div>
</body>
</html>
```